Business card for a new innovative and professional lawn care business

We need a business card design for a new lawn care business in Halifax NS Canada. We offer lawn services in Halifax & Bedford. Our services offered include lawn care, garden services, and property maintenance. We take pride in our work and are experienced at what we do. I would like to see a design that is double sided. On the backside I would like the something simple (maybe my logo preferably on blackround (linked below) with website link, Facebook page or something). The front I want to include contact info:
Darren Maple
phone 902-555-0148
email - darrensyardworks.ca
facebook - Facebook.com/darrensyardworks
Instagram maybe ? - instagram.com/darrenyardworks
Serving Halifax and Bedford for 5 years?
I don't want it to have too much information as I will be passing them out in aim to visit website, or call !
We do want it to include lawn care, garden services and property maintenance.
Basic, catchy, and modern looking !
Logo attached below !

Target Market(s)

Passing business cards to everyone I meet or interact with.

Industry/Entity Type

Lawn Care

Contact Information for Business Card

Double sided with some basic information, with catchy colours and easy to look at.

Font styles to use
Sans Serif

Requirements
Must have
• Must be double sided and have :
• Name, Phone, Email, FB, Website, and 3 main services offered - lawn care, property maintenance, garden services
Nice to have
• Would be nice to have instagram link if it goes well on there
Should not have
• Don't want too much writing or images that are distracting

```html
<!DOCTYPE html>
<html lang="en">
<head>
<meta charset="UTF-8">
<title>Darren's Yardworks – Business Card</title>
<link href="https://fonts.googleapis.com/css2?family=Open+Sans:wght@400;600;700;800&display=swap" rel="stylesheet">
<style>
  :root {
    --backdrop: #3b3532;
    --card: #161616;
    --card-edge: #0d0d0d;
    --green: #1f9a4e;
    --leaf: #5cc24a;
    --white: #f2f2f2;
    --muted: #d8d8d8;
    --rule: #8a8a8a;
  }
  * { margin: 0; padding: 0; box-sizing: border-box; }
  html, body {
    width: 1200px; height: 814px; overflow: hidden;
    background: var(--backdrop);
    font-family: "Open Sans", Arial, sans-serif;
  }
  .canvas {
    width: 1200px; height: 814px;
    display: flex; align-items: center; justify-content: center; gap: 56px;
  }
  .card {
    width: 532px; height: 304px;
    background: var(--card);
    border: 1px solid var(--card-edge);
    box-shadow: 0 10px 24px rgba(0,0,0,.45);
    position: relative;
  }
  /* Front: contact side */
  .mower-art {
    position: absolute; left: 52px; top: 64px;
    width: 186px; height: 196px;
    background: linear-gradient(160deg, #22a457, #137a3a);
    border-radius: 6px;
  }
  .divider {
    position: absolute; left: 268px; top: 78px;
    width: 1px; height: 150px;
    background: linear-gradient(var(--card), var(--rule) 30%, var(--rule) 70%, var(--card));
  }
  .contact { position: absolute; left: 286px; top: 76px; }
  .contact .name {
    color: var(--green); font-weight: 600; font-size: 17px; margin-bottom: 6px;
  }
  .contact ul { list-style: none; }
  .contact li {
    display: flex; align-items: center; gap: 8px;
    color: var(--white); font-size: 12.5px; line-height: 21px;
  }
  .contact svg { width: 12px; height: 12px; flex: none; }
  /* Back: brand side */
  .brand {
    position: absolute; left: 0; right: 0; top: 92px;
    text-align: center;
  }
  .brand .wordmark {
    color: var(--white); font-weight: 800; font-size: 40px;
    letter-spacing: 1px; text-transform: uppercase; line-height: 1;
  }
  .services {
    position: absolute; left: 0; right: 0; top: 206px;
    display: flex; justify-content: center; align-items: center; gap: 6px;
    color: var(--muted); font-size: 12px;
  }
  .services svg { width: 11px; height: 11px; }
</style>
</head>
<body>
<main class="canvas">
  <section class="card card-front">
    <div class="mower-art" role="img" aria-label="Green silhouette of a push lawn mower"></div>
    <div class="divider"></div>
    <div class="contact">
      <p class="name">Darren Maple</p>
      <ul>
        <li>
          <svg viewBox="0 0 12 12"><path fill="var(--green)" d="M2.5 1l2 2-1 1.5c.8 1.6 1.9 2.7 3.5 3.5L8.5 7l2 2-1.5 2C5 10.5 1.5 7 1 3z"/></svg>
          902-555-0148
        </li>
        <li>
          <svg viewBox="0 0 12 12"><rect x="0.5" y="2" width="11" height="8" fill="var(--green)"/><path d="M1 2.5l5 4 5-4" stroke="var(--card)" fill="none"/></svg>
          info@darrensyardworks.ca
        </li>
        <li>
          <svg viewBox="0 0 12 12"><circle cx="6" cy="6" r="5.5" fill="var(--green)"/></svg>
          darrensyardworks.ca
        </li>
        <li>
          <svg viewBox="0 0 12 12"><rect width="12" height="12" rx="1.5" fill="var(--green)"/></svg>
          darrensyardworks
        </li>
        <li>
          <svg viewBox="0 0 12 12"><rect width="12" height="12" rx="1.5" fill="var(--green)"/></svg>
          darrenyardworks
        </li>
      </ul>
    </div>
  </section>

  <section class="card card-back">
    <div class="brand">
      <p class="wordmark">Darren's Yardworks</p>
    </div>
    <div class="services">
      <span>Lawn Care</span>
      <svg viewBox="0 0 12 12"><path d="M1.5 6.5l3 3 6-7" stroke="var(--leaf)" stroke-width="2.2" fill="none"/></svg>
      <span>Property Maintenance</span>
      <svg viewBox="0 0 12 12"><path d="M1.5 6.5l3 3 6-7" stroke="var(--leaf)" stroke-width="2.2" fill="none"/></svg>
      <span>Garden Services</span>
    </div>
  </section>
</main>
</body>
</html>
```